Physical Therapy Center for children Business Card

We need a Business Card for our company (Physical Therapy for children and youth with special needs) in Lisbon, Portugal. The name of the company is "Ninho de Luz"

The card must contain the following info:
- Logo: see uploaded file
- Name: Ninho de Luz
- Slogan: Semeamos Amor, colhemos sorrisos, distribuímos vitórias!
- Service: Terapias Especializadas
- Address: Rua Henrique Lobato Farinha 9C
- ZipCode: 2741-318 Vale da Ribeira
- E-mail: geral@velado.pt
- Site: www.velado.pt
- Facebook: www.facebook.com/ninhodeluz
- Phone: +351 21 584 62 07
- Cell Phone: +351 96 731 84 25

The stationary should have contain all info from business card.

Target Market(s)

Parents of children with special needs

Industry/Entity Type

Physical Therapy

Contact Information for Business Card

The card design should be compatible with http://www.quellprensa.com/product2/order_detail.php?gid=40

Requirements
Should not have
• The business card should not have a Black background. Use white or other color.

```html
<!DOCTYPE html>
<html lang="pt">
<head>
<meta charset="utf-8">
<title>Ninho de Luz – Cartão de Visita</title>
<link rel="stylesheet" href="https://fonts.googleapis.com/css2?family=Questrial&display=swap">
<style>
  :root {
    --page: #e9ecee;
    --card: #ffffff;
    --red: #e8453c;
    --teal: #22b5a0;
    --yellow: #f5c518;
    --ink: #1f1f1f;
    --white: #ffffff;
  }
  * { margin: 0; padding: 0; box-sizing: border-box; }
  html, body {
    width: 1200px;
    height: 900px;
    overflow: hidden;
    background: var(--page);
    font-family: "Questrial", "Century Gothic", sans-serif;
  }
  .card {
    position: absolute;
    left: 282px;
    top: 288px;
    width: 666px;
    height: 375px;
    background: var(--card);
    border-radius: 22px;
    box-shadow: 0 10px 30px rgba(0,0,0,0.12);
    overflow: hidden;
  }
  .brand-mark {
    position: absolute;
    left: 58px;
    top: 130px;
    display: flex;
    align-items: center;
    gap: 10px;
    white-space: nowrap;
  }
  .brand-dot {
    width: 24px;
    height: 24px;
    border-radius: 50%;
    background: var(--teal);
    flex: none;
  }
  .brand-name {
    color: var(--teal);
    font-size: 26px;
    line-height: 1;
  }
  .details {
    position: absolute;
    left: 308px;
    top: 74px;
    color: var(--ink);
    white-space: nowrap;
  }
  .company {
    color: var(--red);
    font-size: 27px;
    font-weight: 700;
    line-height: 1.1;
  }
  .person {
    font-size: 22px;
    line-height: 1.2;
  }
  .phone {
    margin-top: 14px;
    font-size: 17px;
  }
  .address {
    margin-top: 12px;
    font-size: 17px;
    line-height: 1.4;
    font-style: normal;
  }
  .service-band {
    position: absolute;
    left: 0;
    top: 285px;
    width: 606px;
    height: 28px;
    background: var(--teal);
    color: var(--white);
    font-size: 19px;
    line-height: 28px;
    padding-left: 208px;
    white-space: nowrap;
  }
  .accent-block {
    position: absolute;
    left: 606px;
    top: 285px;
    width: 60px;
    height: 28px;
    background: var(--yellow);
  }
  .contact-band {
    position: absolute;
    left: 0;
    top: 313px;
    width: 666px;
    height: 62px;
    background: var(--red);
    display: flex;
    align-items: center;
    justify-content: flex-end;
    gap: 14px;
    padding-right: 44px;
    color: var(--white);
    font-size: 18px;
    white-space: nowrap;
  }
  .contact-item {
    display: flex;
    align-items: center;
    gap: 7px;
  }
  .contact-icon {
    width: 28px;
    height: 28px;
    border-radius: 50%;
    background: var(--white);
    display: flex;
    align-items: center;
    justify-content: center;
    flex: none;
  }
</style>
</head>
<body>
  <article class="card">
    <div class="brand-mark">
      <span class="brand-dot"></span>
      <span class="brand-name">Ninho de Luz</span>
    </div>

    <div class="details">
      <h1 class="company">Ninho de Luz</h1>
      <p class="person">Marta Figueiredo</p>
      <p class="phone">+351 96 731 84 25</p>
      <address class="address">
        Rua Henrique Lobato Farinha 9C<br>
        2741-318 Vale da Ribeira
      </address>
    </div>

    <div class="service-band">Terapias Especializadas</div>
    <div class="accent-block"></div>

    <div class="contact-band">
      <span class="contact-item">
        <span class="contact-icon">
          <svg width="18" height="18" viewBox="0 0 18 18" aria-hidden="true">
            <circle cx="9" cy="9" r="7" fill="none" stroke="#e8453c" stroke-width="1.6"/>
            <ellipse cx="9" cy="9" rx="3" ry="7" fill="none" stroke="#e8453c" stroke-width="1.4"/>
            <line x1="2" y1="9" x2="16" y2="9" stroke="#e8453c" stroke-width="1.4"/>
          </svg>
        </span>
        www.velado.pt
      </span>
      <span class="contact-item">
        <span class="contact-icon"></span>
        ninhodeluz
      </span>
      <span class="contact-item">
        <span class="contact-icon">
          <svg width="16" height="12" viewBox="0 0 16 12" aria-hidden="true">
            <rect x="0" y="0" width="16" height="12" rx="1.5" fill="#e8453c"/>
            <polyline points="1,1.5 8,7 15,1.5" fill="none" stroke="#ffffff" stroke-width="1.4"/>
          </svg>
        </span>
        geral@velado.pt
      </span>
    </div>
  </article>
</body>
</html>
```